The Neighbors Together Project

For submission to Civic Drive 2024
Need both Color and Black and White Versions
TITLE The Neighbours Together Project
Slogan; "Neighbor's Together, same hopes...same Dreams, just a shades difference" -LM Brenner copyrights
Logo in Color and Logo in Black and White
Back of flyer will be The River of Quiet Lights poem -LM Brenner
VOTE BLUE 2024 Header or Footer

I just want to thank you all for your participation in The Neighbours Together Project. In the next few days I will be reducing the choices down to 10. Id like for all of you to know Ive enjoyed seeing so many options and views on the Flyer. Mainly, I wanted to say to those who don't make the cut that I appreciate the work you've done.

LM Doverly

```html
<!DOCTYPE html>
<html lang="en">
<head>
<meta charset="utf-8">
<title>Vote Blue 2024 – Neighbor's Together Flyer</title>
<link rel="stylesheet" href="https://fonts.googleapis.com/css2?family=Ultra&family=Barlow:wght@400;500;600&display=swap">
<style>
  :root {
    --backdrop: #9b9b9b;
    --gold: #cbb57d;
    --gold-text: #d6bf82;
    --navy-top: #2a3d52;
    --navy-bottom: #131f36;
    --red: #b2444a;
    --red-dark: #8a3238;
    --white: #f4f1ea;
    --steel: #5e87aa;
  }
  * { box-sizing: border-box; margin: 0; padding: 0; }
  html, body { width: 1200px; height: 800px; overflow: hidden; }
  body { background: var(--backdrop); font-family: "Barlow", sans-serif; position: relative; }

  .flyer {
    position: absolute; top: 80px; width: 470px; height: 640px;
    background: var(--gold); padding: 14px;
  }
  .flyer--front { left: 95px; }
  .flyer--back { left: 635px; }
  .flyer__panel {
    position: relative; width: 100%; height: 100%;
    background: linear-gradient(180deg, var(--navy-top), var(--navy-bottom));
    overflow: hidden;
  }

  .corner-mark { position: absolute; width: 30px; height: 20px; }
  .corner-mark line { stroke: var(--red); stroke-width: 2.5; }

  .headline {
    position: absolute; left: 0; right: 0; text-align: center;
    font-family: "Ultra", serif; color: var(--gold-text);
    font-size: 34px; letter-spacing: 1px; line-height: 36px; white-space: nowrap;
  }
  .headline--top { top: 30px; }
  .headline--bottom { top: 548px; }

  .ribbon-art { position: absolute; left: 0; width: 100%; }
  .ribbon-art--upper { top: 96px; height: 100px; }
  .ribbon-art--lower { top: 402px; height: 112px; }
  .ribbon-art polygon { fill: var(--red); }
  .ribbon-art .fold { fill: var(--red-dark); }

  .ribbon-title {
    position: absolute; left: 0; right: 0; text-align: center;
    font-family: "Ultra", serif; color: var(--white); letter-spacing: 0.5px;
    white-space: nowrap; line-height: 1;
  }
  .ribbon-title--upper { top: 114px; font-size: 19px; }
  .ribbon-title--lower { top: 478px; font-size: 15px; }

  .tagline {
    position: absolute; left: 0; right: 0; text-align: center;
    color: var(--white); font-weight: 500; font-size: 16px; letter-spacing: 1px; line-height: 1;
  }
  .tagline--hopes { top: 152px; }
  .tagline--dreams { top: 436px; }
  .tagline .dots { color: var(--steel); font-size: 9px; letter-spacing: 3px; vertical-align: middle; margin: 0 8px; }

  .hero-illustration {
    position: absolute; left: 60px; top: 202px; width: 322px; height: 196px;
    background:
      linear-gradient(180deg, rgba(19,31,54,0) 55%, rgba(19,31,54,0.6) 100%),
      linear-gradient(100deg, #4d4f86 0%, #b8b3b6 30%, #b2444a 52%, #e6e0dc 70%, #9c2f3a 100%);
    border-radius: 6px 40px 4px 4px;
  }

  .poem-title {
    position: absolute; top: 88px; left: 0; right: 0; text-align: center;
    font-family: "Ultra", serif; color: var(--gold-text); font-size: 22px; letter-spacing: 0.5px;
  }
  .poem-author {
    position: absolute; top: 120px; left: 0; right: 0; text-align: center;
    color: var(--white); font-size: 11px; font-weight: 500;
  }
  .poem {
    position: absolute; top: 172px; left: 24px; right: 24px; text-align: center;
    color: var(--white); font-size: 12.5px; font-weight: 500; line-height: 1.75;
  }
  .poem p { margin-bottom: 22px; }
  .site-address {
    position: absolute; bottom: 62px; left: 0; right: 0; text-align: center;
    color: var(--gold-text); font-size: 12px; font-weight: 600; letter-spacing: 0.5px;
  }
</style>
</head>
<body>

<section class="flyer flyer--front">
  <div class="flyer__panel">
    <svg class="corner-mark" style="left:18px;top:38px" viewBox="0 0 30 20"><line x1="4" y1="3" x2="28" y2="3"/><line x1="10" y1="10" x2="28" y2="10"/><line x1="2" y1="17" x2="28" y2="17"/></svg>
    <svg class="corner-mark" style="right:18px;top:38px" viewBox="0 0 30 20"><line x1="2" y1="3" x2="26" y2="3"/><line x1="2" y1="10" x2="20" y2="10"/><line x1="2" y1="17" x2="28" y2="17"/></svg>
    <h1 class="headline headline--top">VOTE BLUE 2024</h1>

    <svg class="ribbon-art ribbon-art--upper" viewBox="0 0 442 100" preserveAspectRatio="none">
      <polygon class="fold" points="70,26 100,26 100,54 70,50"/>
      <polygon points="40,30 82,24 82,62 58,56"/>
      <polygon class="fold" points="342,26 372,26 372,50 342,54"/>
      <polygon points="360,24 402,30 384,56 360,62"/>
      <polygon points="82,10 360,10 360,48 82,48"/>
      <polygon points="30,94 412,80 428,84 412,88 30,100"/>
    </svg>
    <div class="ribbon-title ribbon-title--upper">NEIGHBOR'S TOGETHER</div>
    <div class="tagline tagline--hopes"><span class="dots">◆◆◆</span>SAME HOPES<span class="dots">◆◆◆</span></div>

    <div class="hero-illustration" role="img" aria-label="Illustration of a waving American flag shaped like the map of the United States, with a diverse group of people seen from behind, arms around each other"></div>

    <svg class="ribbon-art ribbon-art--lower" viewBox="0 0 442 112" preserveAspectRatio="none">
      <polygon points="14,18 420,4 410,12 30,24"/>
      <polygon class="fold" points="60,66 90,64 90,98 60,94"/>
      <polygon points="34,64 76,62 72,102 48,90"/>
      <polygon class="fold" points="352,64 382,66 382,94 352,98"/>
      <polygon points="366,62 408,64 394,90 370,102"/>
      <polygon points="76,60 366,60 366,100 76,100"/>
    </svg>
    <div class="tagline tagline--dreams"><span class="dots">◆◆◆</span>SAME DREAMS<span class="dots">◆◆◆</span></div>
    <div class="ribbon-title ribbon-title--lower">JUST A SHADES DIFFERENCE</div>

    <h2 class="headline headline--bottom">VOTE BLUE 2024</h2>
    <svg class="corner-mark" style="left:18px;bottom:18px" viewBox="0 0 30 20"><line x1="4" y1="3" x2="28" y2="3"/><line x1="10" y1="10" x2="28" y2="10"/><line x1="2" y1="17" x2="28" y2="17"/></svg>
    <svg class="corner-mark" style="right:18px;bottom:18px" viewBox="0 0 30 20"><line x1="2" y1="3" x2="26" y2="3"/><line x1="2" y1="10" x2="20" y2="10"/><line x1="2" y1="17" x2="28" y2="17"/></svg>
  </div>
</section>

<section class="flyer flyer--back">
  <div class="flyer__panel">
    <svg class="corner-mark" style="right:18px;top:26px" viewBox="0 0 30 20"><line x1="2" y1="3" x2="26" y2="3"/><line x1="2" y1="10" x2="20" y2="10"/><line x1="2" y1="17" x2="28" y2="17"/></svg>
    <h1 class="poem-title">RIVER OF QUIET LIGHTS</h1>
    <p class="poem-author">By LM Brenner</p>
    <div class="poem">
      <p>From river towns to city lights and porches in the rain,<br>we gather at the water's edge and call each other's name.</p>
      <p>We are a stream of many voices...soft and bright, old and new,<br>forever flowing onward with a steady, patient view.</p>
      <p>We have walked from distant valleys, carried lanterns through the<br>night. Sharing bread and open doorways...keeping every window bright.</p>
      <p>Free to speak, Free to listen, Free to build or Free to<br>rest...lending, learning side by side in this quiet place we're<br>blessed.</p>
      <p>We must always lift each other, keep the lanterns burning on.<br>For together we are morning and alone we're merely dawn</p>
    </div>
    <p class="site-address">WWW.NEIGHBORSTOGETHERPROJECT.ORG</p>
    <svg class="corner-mark" style="right:18px;bottom:24px" viewBox="0 0 30 20"><line x1="2" y1="3" x2="26" y2="3"/><line x1="2" y1="10" x2="20" y2="10"/><line x1="2" y1="17" x2="28" y2="17"/></svg>
    <svg class="corner-mark" style="left:18px;bottom:24px" viewBox="0 0 30 20"><line x1="4" y1="3" x2="28" y2="3"/><line x1="10" y1="10" x2="28" y2="10"/><line x1="2" y1="17" x2="28" y2="17"/></svg>
  </div>
</section>

</body>
</html>
```